Harriet Voss Consortium - Paediatric Lower Limb Surgery Agenda Forming Collective

A 2-sided A4 leaflet to explain the research priorities in Children's Orthopaedic Surgery.
We would like this to be similar to that produced previously by the physiotherapists.

```html
<!DOCTYPE html>
<html lang="en">
<head>
<meta charset="utf-8">
<title>Harriet Voss Consortium – Research Priorities Leaflet</title>
<link rel="stylesheet" href="https://fonts.googleapis.com/css2?family=Lato:ital,wght@0,300;0,400;0,700;1,400;1,700&family=Roboto+Condensed:wght@700&display=swap">
<style>
  :root {
    --red: #e3263a;
    --blue: #47a0da;
    --yellow: #f2e31b;
    --gold: #fbd93a;
    --maroon: #8b1c2c;
    --ink: #3a3a3a;
    --grey-text: #5c5c5c;
    --backdrop: #e6e6e6;
    --paper: #ffffff;
    --crest: #8a7a9e;
  }
  * { box-sizing: border-box; margin: 0; padding: 0; }
  html, body { width: 1200px; height: 1000px; overflow: hidden; }
  body {
    background: var(--backdrop);
    font-family: "Lato", Arial, sans-serif;
    position: relative;
  }
  .page {
    position: absolute;
    top: 117px;
    height: 765px;
    background: var(--paper);
    overflow: hidden;
  }
  .page--front { left: 40px; width: 552px; }
  .page--back { left: 607px; width: 540px; }
  .abs { position: absolute; }

  /* Front page */
  .year {
    left: 25px; top: 18px;
    font-size: 72px; font-weight: 400; color: var(--red); line-height: 1;
  }
  .brand-mark {
    right: 16px; top: 22px; width: 170px;
    display: flex; align-items: center; gap: 8px;
  }
  .brand-mark__square { width: 34px; height: 34px; background: var(--maroon); flex: none; }
  .brand-mark__name { font-size: 21px; line-height: 1.05; color: var(--maroon); font-weight: 400; }
  .title-main {
    left: 24px; top: 98px;
    font-family: "Roboto Condensed", "Arial Narrow", sans-serif;
    font-size: 38px; color: var(--red); line-height: 1;
  }
  .title-sub {
    left: 24px; top: 146px; width: 520px;
    font-family: "Roboto Condensed", "Arial Narrow", sans-serif;
    font-size: 30px; color: var(--blue); line-height: 1.3;
  }
  .intro {
    left: 22px; width: 508px;
    font-style: italic; font-size: 12.5px; line-height: 1.32;
    color: var(--grey-text); text-align: center;
  }
  .intro--one { top: 233px; }
  .intro--two { top: 298px; }
  .intro--three { left: 258px; top: 367px; width: 280px; }
  .blobs { left: 0; top: 0; width: 552px; height: 765px; }
  .stage { text-align: center; }
  .stage__label { font-weight: 700; font-size: 12.5px; text-align: left; }
  .stage__verb { font-style: italic; font-size: 27px; line-height: 1.1; }
  .stage__body { font-size: 12.5px; line-height: 1.28; }
  .stage--ask { left: 18px; top: 378px; width: 228px; color: #fff; }
  .stage--ask .stage__label { padding-left: 26px; }
  .stage--ask .stage__body { font-size: 12px; line-height: 1.25; }
  .stage--analyse { left: 278px; top: 451px; width: 246px; color: #fff; }
  .stage--analyse .stage__label { padding-left: 30px; }
  .stage--prioritise { left: 92px; top: 566px; width: 292px; color: var(--ink); }
  .stage--prioritise .stage__label { padding-left: 8px; }
  .stage--prioritise .stage__verb { color: #555; }
  .partner {
    display: flex; align-items: center; gap: 6px;
  }
  .partner--uni {
    left: 162px; top: 711px; width: 148px; height: 48px;
    background: #fff; border: 1px solid #ccc; padding: 0 8px;
  }
  .partner--uni .partner__square { width: 26px; height: 26px; background: #1d2d5a; flex: none; }
  .partner--uni .partner__name { font-size: 12.5px; line-height: 1.1; color: #1d2d5a; font-weight: 700; }
  .partner--society {
    left: 318px; top: 718px; width: 132px; height: 30px;
    background: #fff; border-radius: 8px; padding: 0 8px;
  }
  .partner--society .partner__square { width: 14px; height: 14px; background: var(--red); flex: none; }
  .partner--society .partner__name { font-size: 10px; line-height: 1.1; color: var(--red); font-weight: 700; }
  .partner-badge {
    left: 462px; top: 680px; width: 60px; height: 70px;
    background: var(--crest); border-radius: 6px 6px 30px 30px; opacity: .85;
  }

  /* Back page */
  .priorities-head {
    left: 0; top: 20px; width: 540px;
    display: flex; justify-content: center; align-items: center; gap: 16px;
  }
  .priorities-head__title {
    font-family: "Roboto Condensed", "Arial Narrow", sans-serif;
    font-size: 23px; color: var(--red);
  }
  .priorities-head__icon { width: 42px; height: 32px; }
  .band { left: 0; width: 540px; z-index: 0; }
  .band--gold { background: var(--gold); }
  .band--blue { background: var(--blue); }
  .band--red { background: var(--red); }
  .cut-top-left { clip-path: polygon(32% 0, 100% 0, 100% 100%, 0 100%, 0 85%); }
  .cut-top-right { clip-path: polygon(0 0, 68% 0, 100% 85%, 100% 100%, 0 100%); }
  .priority {
    font-size: 12.5px; line-height: 1.3; color: var(--ink); z-index: 1;
  }
  .priority--light { color: #fff; }
  .num {
    font-size: 42px; font-weight: 300; line-height: 1; z-index: 2;
  }
  .num--gold { color: var(--gold); }
  .num--blue { color: var(--blue); }
  .num--red { color: var(--red); }
  .thanks {
    left: 20px; top: 681px; width: 500px;
    text-align: center; color: var(--red); font-weight: 700; font-size: 13px; line-height: 1.3;
  }
  .credits-label {
    left: 9px; top: 726px; font-style: italic; color: var(--red); font-size: 10px;
  }
  .credits {
    left: 105px; top: 729px; font-style: italic; color: var(--red); font-size: 7.5px; line-height: 1.45;
    list-style: none;
  }
</style>
</head>
<body>

<section class="page page--front">
  <svg class="abs blobs" viewBox="0 0 552 765" aria-hidden="true">
    <path d="M0 378 C60 366 190 362 240 372 C268 378 266 430 260 480 C254 525 230 548 150 552 C80 555 30 560 0 565 Z" fill="var(--red)"/>
    <path d="M300 450 C340 430 430 420 500 418 C530 417 552 420 552 420 L552 765 L300 765 C285 640 262 480 300 450 Z" fill="var(--blue)"/>
    <path d="M0 548 C40 532 140 530 230 548 C320 566 400 600 395 660 C392 700 360 730 330 765 L0 765 Z" fill="var(--yellow)"/>
  </svg>

  <div class="abs year">2019</div>
  <div class="abs brand-mark">
    <span class="brand-mark__square"></span>
    <span class="brand-mark__name">Harriet Voss Consortium</span>
  </div>

  <h1 class="abs title-main">Harriet Voss Consortium</h1>
  <h2 class="abs title-sub">Paediatric Lower Limb Surgery Agenda Forming Collective</h2>

  <p class="abs intro intro--one">Surgery is often carried out amongst children with conditions that their legs, but in many conditions, it is not known which treatment works best. We need high-quality research to test which treatments are better for children.</p>
  <p class="abs intro intro--two">We reached out to everybody involved with children who have orthopaedic problems affecting their legs (from hip to toes), including children, parents, carers, charity workers, and all the professional group.</p>
  <p class="abs intro intro--three">We asked all for their views on identifying the most important unanswered questions.</p>

  <div class="abs stage stage--ask">
    <p class="stage__label">STAGE 1</p>
    <p class="stage__verb">ASK</p>
    <p class="stage__body">Our UK-wide survey of patients, carers, physiotherapists, nurses and surgeons asked “What is the most important unanswered question amongst children undergoing planned surgery for conditions affecting their legs”</p>
  </div>
  <div class="abs stage stage--analyse">
    <p class="stage__label">STAGE 2</p>
    <p class="stage__verb">ANALYSE</p>
    <p class="stage__body">We reviewed 1023 questions from 388 people, and sorted these into 76 unique themed questions.</p>
  </div>
  <div class="abs stage stage--prioritise">
    <p class="stage__label">STAGE 3</p>
    <p class="stage__verb">PRIORITISE</p>
    <p class="stage__body">From those we asked patients, carers, physiotherapists, nurses and surgeons to tell us “What are your top-10 most important questions”. This created a shortlist that were prioritized at a final workshop.</p>
  </div>

  <div class="abs partner partner--uni">
    <span class="partner__square"></span>
    <span class="partner__name">University of Halbrook</span>
  </div>
  <div class="abs partner partner--society">
    <span class="partner__square"></span>
    <span class="partner__name">Kestrel Society</span>
  </div>
  <div class="abs partner-badge" role="img" aria-label="Partner association badge"></div>
</section>

<section class="page page--back">
  <header class="abs priorities-head">
    <svg class="priorities-head__icon" viewBox="0 0 42 32" aria-hidden="true">
      <rect x="14" y="0" width="14" height="8" rx="2" fill="var(--red)"/>
      <path d="M19 8 L21 11 L23 8 Z" fill="var(--red)"/>
      <circle cx="9" cy="16" r="4" fill="var(--red)"/><circle cx="21" cy="15" r="4.5" fill="var(--red)"/><circle cx="33" cy="16" r="4" fill="var(--red)"/>
      <path d="M2 32 C2 24 16 24 16 32 Z M13 32 C13 22 29 22 29 32 Z M26 32 C26 24 40 24 40 32 Z" fill="var(--red)"/>
    </svg>
    <h2 class="priorities-head__title">Our top-10 research priorities</h2>
    <svg class="priorities-head__icon" viewBox="0 0 42 32" aria-hidden="true">
      <rect x="14" y="0" width="14" height="8" rx="2" fill="var(--red)"/>
      <path d="M19 8 L21 11 L23 8 Z" fill="var(--red)"/>
      <circle cx="9" cy="16" r="4" fill="var(--red)"/><circle cx="21" cy="15" r="4.5" fill="var(--red)"/><circle cx="33" cy="16" r="4" fill="var(--red)"/>
      <path d="M2 32 C2 24 16 24 16 32 Z M13 32 C13 22 29 22 29 32 Z M26 32 C26 24 40 24 40 32 Z" fill="var(--red)"/>
    </svg>
  </header>

  <div class="abs band band--gold cut-top-left" style="top:58px;height:69px"></div>
  <span class="abs num num--gold" style="left:14px;top:60px">1</span>
  <p class="abs priority" style="left:121px;top:76px;width:400px">What are the best ways to measure the outcome following lower limb orthopaedic surgery in children?</p>

  <p class="abs priority" style="left:20px;top:134px;width:460px">Following orthopaedic surgery to the lower limbs, what should children’s rehabilitation include, how long is it expected to last and how does it affect the result of treatment?</p>
  <span class="abs num num--blue" style="left:492px;top:134px">2</span>

  <span class="abs num num--blue" style="left:20px;top:198px">3</span>
  <p class="abs priority" style="left:68px;top:194px;width:455px">What is the short-term and long-term clinical and cost effectiveness of orthopaedic lower limb surgery (including best timing and technique) for children with Cerebral Palsy who can walk?</p>

  <div class="abs band band--blue cut-top-right" style="top:248px;height:68px"></div>
  <span class="abs num num--blue" style="left:500px;top:250px">4</span>
  <p class="abs priority priority--light" style="left:15px;top:266px;width:400px">What are the short term and long term outcomes of surgery compared to non-surgical care in the treatment of Perthes disease of the hip?</p>

  <div class="abs band band--red cut-top-left" style="top:318px;height:68px"></div>
  <span class="abs num num--red" style="left:14px;top:320px">5</span>
  <p class="abs priority priority--light" style="left:121px;top:334px;width:405px">What is the clinical and cost effectiveness of pre-operative rehabilitation in children presenting with lower limb orthopaedic conditions?</p>

  <p class="abs priority" style="left:20px;top:394px;width:460px">What is the short-term and long-term clinical and cost effectiveness of Selective Dorsal Rhizotomy (SDR) in children with Cerebral Palsy who can walk?</p>
  <span class="abs num num--blue" style="left:492px;top:390px">6</span>

  <span class="abs num num--blue" style="left:20px;top:440px">7</span>
  <p class="abs priority" style="left:63px;top:436px;width:462px">Can surveillance and non-surgical treatment (e.g. physiotherapy, botulinum toxin injections, functional electrical stimulation, orthotics, casting) prevent the development of deformity requiring surgery in children with Cerebral Palsy?</p>

  <p class="abs priority" style="left:20px;top:492px;width:460px">What is the best method of screening for Developmental Dysplasia of the Hip (DDH) in terms of clinical and cost effectiveness?</p>
  <span class="abs num num--blue" style="left:492px;top:488px">8</span>

  <div class="abs band band--gold cut-top-left" style="top:537px;height:68px"></div>
  <span class="abs num num--gold" style="left:14px;top:539px">9</span>
  <p class="abs priority" style="left:121px;top:551px;width:405px">What are the best strategies to optimise communication of information between patients/carers and clinicians in order to enable shared decision-making?</p>

  <div class="abs band band--red cut-top-right" style="top:606px;height:70px"></div>
  <span class="abs num num--red" style="left:478px;top:608px">10</span>
  <p class="abs priority priority--light" style="left:15px;top:625px;width:380px">What is the best management for hip displacement in children with Cerebral Palsy?</p>

  <p class="abs thanks">Many thanks to all those people who helped us take this work off the ground and helped us finish it!</p>
  <p class="abs credits-label">Special thanks to:</p>
  <ul class="abs credits">
    <li>The Kestrel Society of Children’s Orthopaedic Surgery ,</li>
    <li>The Northgate Orthopaedic Association</li>
    <li>The University of Halbrook and the Harriet Voss Consortium, who always look for fair play in research!</li>
  </ul>
</section>

</body>
</html>
```